Law Firm Needs a Stationery Design

We need a stationery design for a law firm based in the East African region called 'Mbogoreto Lwanyika & Company Advocates'. We are a law firm specializing in commercial, public and constitutional law. Our practice areas include Telecommunications Law, Mining Law, Oil and Energy Law, Real Estate and Land Development Law, Employment Law, Family Law, Civil and Criminal Litigation, Constitutional Law, Company Secretariat and more. We represent a wide variety of clients, ranging from individuals to corporations and approach each case with full attention, dedication and legal acumen in order to protect the interests of our clients. The final stationary design should communicate innovation and expertise to meet our clients’ legal needs.
Target Market(s)
New clients, current and former clients, other lawyers in and outside of our practice area, or other professionals, contacts and centers of influence within the region
Industry/Entity Type
Real Estate
Colors
Designer to choose colors to be used in the design.
Look and feel

```html
<!DOCTYPE html>
<html lang="en">
<head>
<meta charset="utf-8">
<title>Mbogoreto Lwanyika &amp; Company Advocates — Stationery</title>
<link rel="stylesheet" href="https://fonts.googleapis.com/css2?family=Roboto+Slab:wght@300&family=Open+Sans:wght@400&display=swap">
<style>
  :root {
    --gold: #b39260;
    --gold-deep: #9a7638;
    --charcoal: #3a3839;
    --ink: #333132;
    --paper: #ffffff;
    --edge: #cfcfcf;
    --label: #222222;
    --caption: #7a7a7a;
    --slab: "Roboto Slab", Georgia, serif;
    --sans: "Open Sans", Arial, sans-serif;
  }
  * { box-sizing: border-box; margin: 0; padding: 0; }
  html, body { width: 1200px; height: 770px; overflow: hidden; background: var(--paper); }
  .board { position: relative; width: 1200px; height: 770px; font-family: var(--sans); }

  .label { position: absolute; font-size: 9px; color: var(--label); white-space: nowrap; }
  .caption { position: absolute; left: 642px; top: 732px; font-size: 15px; color: var(--caption); white-space: nowrap; }

  .sheet { position: absolute; background: var(--paper); border: 1px solid var(--edge); }
  .band { position: absolute; left: 0; top: 0; width: 100%; background: var(--gold); }

  .brand { position: absolute; display: flex; align-items: center; }
  .brand-dot { border-radius: 50%; background: var(--ink); flex: none; }
  .brand-name { font-family: var(--slab); font-weight: 300; color: var(--ink); line-height: 1.02; white-space: nowrap; }
  .brand-name span { display: block; }

  .contact { position: absolute; text-align: right; font-size: 8.6px; line-height: 11.6px; color: var(--ink); white-space: nowrap; }

  /* letterhead */
  .letterhead { left: 91px; top: 85px; width: 426px; height: 601px; }
  .letterhead .band { height: 72px; }
  .letterhead .brand { left: 19px; top: 13px; }
  .letterhead .brand-dot { width: 48px; height: 48px; margin-right: 8px; }
  .letterhead .brand-name { font-size: 21px; }
  .letterhead .brand-name span + span { font-size: 15px; padding-left: 6px; }
  .letterhead .contact { right: 20px; top: 505px; }

  /* business cards */
  .card { position: absolute; top: 197px; height: 104px; }
  .card-front { left: 47px; width: 181px; background: var(--gold); }
  .card-front .brand { left: 11px; top: 36px; }
  .card-front .brand-dot { width: 32px; height: 32px; margin-right: 5px; }
  .card-front .brand-name { font-size: 14px; }
  .card-front .brand-name span + span { font-size: 10.5px; padding-left: 4px; }
  .card-back { left: 245px; width: 182px; background: var(--charcoal); }
  .card-back .seal { position: absolute; left: 8px; top: 13px; width: 78px; height: 78px; border-radius: 50%; background: var(--gold); border: 2px solid #c9ab78; display: flex; flex-direction: column; align-items: center; justify-content: center; font-family: var(--slab); font-weight: 300; font-size: 7.5px; line-height: 10px; color: var(--ink); text-align: center; }
  .card-back .contact { right: 10px; top: 25px; font-size: 6px; line-height: 8.4px; color: #e9e4da; }

  /* complimentary slip */
  .slip { left: 540px; top: 85px; width: 307px; height: 189px; }
  .slip .band { height: 33px; }
  .slip .brand { left: 7px; top: 7px; }
  .slip .brand-dot { width: 20px; height: 20px; margin-right: 4px; }
  .slip .brand-name { font-size: 9.5px; }
  .slip .brand-name span + span { font-size: 7px; padding-left: 2px; }

  /* envelope front */
  .envelope-front { left: 155px; top: 335px; width: 488px; height: 231px; }
  .envelope-front .band { height: 51px; }
  .envelope-front .brand { left: 12px; top: 9px; }
  .envelope-front .brand-dot { width: 33px; height: 33px; margin-right: 4px; }
  .envelope-front .brand-name { font-size: 15px; }
  .envelope-front .brand-name span + span { font-size: 11px; padding-left: 5px; }
  .envelope-front .contact { right: 12px; top: 141px; }

  /* envelope open */
  .envelope-open { position: absolute; left: 665px; top: 255px; width: 489px; height: 309px; }
</style>
</head>
<body>
<main class="board">

  <p class="label" style="left:94px; top:69px;">Letterhead</p>
  <section class="sheet letterhead" aria-label="Letterhead">
    <div class="band"></div>
    <div class="brand">
      <div class="brand-dot"></div>
      <p class="brand-name"><span>Mbogoreto Lwanyika</span><span>&amp; Company Advocates</span></p>
    </div>
    <address class="contact" style="font-style:normal">
      T: 12345 12345<br>E: info@mlca.com<br>W: www.mlca.com<br>Address Line, Lorem ipsum,<br>Dolor sit amet,<br>Consectetuer adipiscing<br>Dolor sit amet- 40021
    </address>
  </section>

  <section class="card card-front" aria-label="Business card front">
    <div class="brand">
      <div class="brand-dot"></div>
      <p class="brand-name"><span>Mbogoreto Lwanyika</span><span>&amp; Company Advocates</span></p>
    </div>
  </section>
  <section class="card card-back" aria-label="Business card back">
    <div class="seal"><span>Mbogoreto Lwanyika</span><span>Principle Lawyer</span></div>
    <address class="contact" style="font-style:normal">
      T: 12345 12345 / 022 1234 1234<br>E: info@mlca.com<br>W: www.mlca.com<br>Address Line, Lorem ipsum,<br>Dolor sit amet,<br>Consectetuer adipiscing<br>Dolor sit amet- 40021
    </address>
  </section>
  <p class="label" style="left:334px; top:306px; font-size:8px;">Business Card (front/back)</p>

  <p class="label" style="left:543px; top:69px;">Complimentary Slip</p>
  <section class="sheet slip" aria-label="Complimentary slip">
    <div class="band"></div>
    <div class="brand">
      <div class="brand-dot"></div>
      <p class="brand-name"><span>Mbogoreto Lwanyika</span><span>&amp; Company Advocates</span></p>
    </div>
  </section>

  <section class="sheet envelope-front" aria-label="Envelope front">
    <div class="band"></div>
    <div class="brand">
      <div class="brand-dot"></div>
      <p class="brand-name"><span>Mbogoreto Lwanyika</span><span>&amp; Company Advocates</span></p>
    </div>
    <address class="contact" style="font-style:normal">
      T: 12345 12345<br>E: info@mlca.com<br>W: www.mlca.com<br>Address Line, Lorem ipsum,<br>Dolor sit amet,<br>Consectetuer adipiscing<br>Dolor sit amet- 40021
    </address>
  </section>

  <svg class="envelope-open" viewBox="0 0 489 309" aria-label="Envelope open">
    <defs>
      <linearGradient id="pocket" x1="0" y1="0" x2="0" y2="1">
        <stop offset="0" stop-color="#c6a56c"/>
        <stop offset="0.6" stop-color="#b08a4c"/>
        <stop offset="1" stop-color="#9a7638"/>
      </linearGradient>
    </defs>
    <rect x="0.5" y="77" width="488" height="231.5" fill="#fff" stroke="#cfcfcf"/>
    <path d="M0 0 H458 Q488 0 488 30 V77 H0 Z" fill="#b39260"/>
    <line x1="0" y1="77.5" x2="488" y2="77.5" stroke="#fff" stroke-width="1"/>
    <path d="M25 78 H463 L452 128 Q447 150 420 150 H68 Q41 150 36 128 Z" fill="url(#pocket)"/>
  </svg>
  <p class="label" style="left:1070px; top:571px;">Envelope (front/open)</p>

  <p class="caption">Concept: Symbol shows Lawyer’s Tie and colours depicts nature of business.</p>
</main>
</body>
</html>
```